INCREASED BUDGET -- Cover Art Template Needed For Record Label

We are an electronic music record label that needs a cover art template for our 2017 releases. The design must be easy to update in Photoshop with different text, colors, or patterns.

The winner will also be asked to design our social media banners for Facebook, Twitter, and SoundCloud, so there's an opportunity to make more money.

Words to describe our sound: sophisticated, forward-thinking, futuristic, modern, emotional

Please make the LA logo the focal point of your design. Feel free to modify our logo as needed. Bonus points for anyone that can find a way to visually represent the word "Lanternfold". Examples of artwork that we found attractive are included to provide inspiration.

You can view our previous releases by clicking on any of the links: https://www.tunevaultshop.example/label/lanternfold-audio/52947/releases

Target Market(s)

Electronic music lovers

Industry/Entity Type

Music Download

Font styles to use
Serif
Decorative
Other font styles liked:
• Aller Display, Aller Light

Requirements
Must have
• Lanternfold Audio record logo
• Name of artist: Rufus Delgarde
• Title: Daybreak / Hold Still (Reworks)
Nice to have
• Tracklist:
• Hold Still (Brantlow Remix)
• Daybreak (Zolvarin Remix)
• Catalog number: 318

```html
<!DOCTYPE html>
<html lang="en">
<head>
<meta charset="utf-8">
<title>Daybreak / Hold Still (Reworks) — Rufus Delgarde</title>
<link href="https://fonts.googleapis.com/css2?family=Montserrat:wght@300;400;500&display=swap" rel="stylesheet">
<style>
  :root {
    --stage: #121315;
    --sleeve: #17161a;
    --sleeve-glow: #2a2629;
    --ink: #ffffff;
    --accent-red: #e8283a;
    --accent-yellow: #e4e23c;
    --label-blue: #2b9bd8;
  }
  * { margin: 0; padding: 0; box-sizing: border-box; }
  html, body {
    width: 1200px; height: 1013px; overflow: hidden;
    background: var(--stage);
    font-family: "Montserrat", sans-serif;
    color: var(--ink);
  }
  .cover {
    position: absolute; left: 130px; top: 36px;
    width: 940px; height: 940px; overflow: hidden;
    background: radial-gradient(ellipse at 50% 45%, var(--sleeve-glow) 0%, var(--sleeve) 70%);
  }
  .cover-art { position: absolute; inset: 0; }
  .release-title {
    position: absolute; top: 33px; left: 0; width: 100%;
    text-align: center; font-weight: 400; font-size: 41px; line-height: 52px; letter-spacing: 0.3px;
  }
  .artist-name {
    position: absolute; top: 97px; left: 0; width: 100%;
    text-align: center; font-weight: 400; font-size: 25px; line-height: 32px;
  }
  .catalog-number {
    position: absolute; left: 239px; top: 792px;
    font-size: 46px; font-weight: 400; color: var(--accent-yellow);
    border-bottom: 2px solid var(--accent-yellow); line-height: 1.05;
  }
  .tracklist {
    position: absolute; left: 239px; top: 857px; list-style: none;
    font-size: 21px; line-height: 30px;
  }
  .track-title { font-weight: 500; }
  .track-remix { font-weight: 300; }
  .label-mark {
    position: absolute; left: 592px; top: 768px;
    display: flex; align-items: center; gap: 16px;
    font-size: 44px; line-height: 50px; font-weight: 500; color: var(--label-blue);
  }
  .label-dot { flex: none; width: 72px; height: 72px; border-radius: 50%; background: var(--label-blue); }
</style>
</head>
<body>
  <main class="cover">
    <svg class="cover-art" width="940" height="940" viewBox="0 0 940 940">
      <defs>
        <radialGradient id="artGlow" cx="55%" cy="45%" r="55%">
          <stop offset="0%" stop-color="#e8283a" stop-opacity="0.95"/>
          <stop offset="60%" stop-color="#c81f30" stop-opacity="0.65"/>
          <stop offset="100%" stop-color="#c81f30" stop-opacity="0"/>
        </radialGradient>
      </defs>
      <ellipse class="artwork-area" role="img" aria-label="Abstract illustration of stacked red rings and white orbit lines floating in speckled space"
               cx="485" cy="420" rx="330" ry="340" fill="url(#artGlow)"/>
    </svg>
    <h1 class="release-title">DAYBREAK / HOLD STILL (REWORKS)</h1>
    <p class="artist-name">Rufus Delgarde</p>
    <p class="catalog-number">318</p>
    <ul class="tracklist">
      <li><span class="track-title">Hold Still</span> <span class="track-remix">(Brantlow Remix)</span></li>
      <li><span class="track-title">Daybreak</span> <span class="track-remix">(Zolvarin Remix)</span></li>
    </ul>
    <div class="label-mark"><span class="label-dot"></span><span>Lanternfold<br>Audio</span></div>
  </main>
</body>
</html>
```